Manuka Honey company needs a Upmarket, Luxury Website!

New Zealand, Taranaki based Manuka Honey company Marumaru Honey is looking for a new website, we are looking for an upmarket, luxury, serious website design. We export the highest quality quality Manuka Honey, straight from the Taranaki region.

Main export markets are Asia & Europe, also New Zealand & Australia.

Looking to have a beautiful, upmarket, serious, luxurious & graphical experience with mobile optimization in mind. Like the use of product staging/mockups

You can use copy from other websites to build the site and we will change the copy after the design is finished.

***Please include 'Honey Product' mockups in website.

*Will add illustrator files in coming days***

Feel free to make website functional in Shopify, Wordpress or WIX

Target Market(s)

Asia, Europe (main markets) New Zealand, Australia (Submarkets)

Coding

Coded - Design and coding required

Number of Pages Required

4 page

Requirements
Must have
• Home, Shop, About Us, Contact Us

Homepage to include:

Our Products
Company Video (video under construction)
What is MGO/UMF
Newsletter Opt-in

***(Not in Order)***

Please include 'Honey Product' mockups in website.
*Will add illustrator files in coming days
Nice to have
• FAQ & Partnership Inquiries (hyperlink in footer)

```html
<!DOCTYPE html>
<html lang="en">
<head>
<meta charset="utf-8">
<title>Marumaru Honey — Handcrafted Manuka Honey</title>
<link rel="stylesheet" href="https://fonts.googleapis.com/css2?family=Amatic+SC:wght@400;700&family=Montserrat:wght@400;500;600;700&display=swap">
<style>
:root{
  --green:#a6c72b;
  --green-dark:#93b31f;
  --ink:#1d1d1d;
  --text:#555;
  --cream:#f7f9ea;
  --hero-top:#f5f6f0;
  --hero-bottom:#d6decb;
  --video-bg:#efecea;
  --purple:#bf96c4;
  --lime:#b6d44e;
  --blue:#7ba1cd;
  --white:#fff;
  --jar-lid:#1b1b1b;
  --jar-gold:#a8892b;
  --jar-gold-dark:#7e6518;
}
*{box-sizing:border-box;margin:0;padding:0}
html,body{width:1200px;height:4871px;overflow:hidden}
body{position:relative;font-family:'Montserrat',sans-serif;color:var(--ink);background:var(--white)}
.abs{position:absolute}
.display{font-family:'Amatic SC',cursive;font-weight:400;letter-spacing:2px;line-height:1;white-space:nowrap}
.btn{position:absolute;display:flex;align-items:center;justify-content:center;font-size:14px;font-weight:700;letter-spacing:.5px;text-transform:uppercase;white-space:nowrap}
.btn-green{background:var(--green);color:var(--white)}
.btn-outline{border:3px solid var(--ink);color:var(--ink);background:transparent;font-size:13px}
.jar{position:absolute;border-radius:14px 14px 20px 20px;background:linear-gradient(180deg,var(--jar-lid) 0 20%,var(--jar-gold) 20%,var(--jar-gold) 70%,var(--jar-gold-dark) 100%);box-shadow:0 12px 24px rgba(0,0,0,.25)}

/* nav */
.nav a{position:absolute;top:62px;font-size:15px;font-weight:600;color:var(--ink);text-decoration:none;letter-spacing:.3px}
.brand{position:absolute;left:529px;top:22px;width:200px;height:110px;display:flex;flex-direction:column;align-items:center;justify-content:center;gap:8px}
.brand .dot{width:28px;height:28px;border-radius:50%;background:var(--ink)}
.brand span{font-size:15px;font-weight:700;letter-spacing:1px;text-transform:uppercase;white-space:nowrap}

/* hero */
.hero{position:absolute;left:0;top:0;width:1200px;height:907px;background:linear-gradient(180deg,var(--hero-top) 0%,var(--hero-top) 30%,var(--hero-bottom) 70%,#eef1e6 100%)}
.hero-clouds{position:absolute;left:0;top:780px;width:1200px;height:127px}
.arrow{position:absolute;width:50px;height:50px;border-radius:50%;background:var(--white);box-shadow:0 2px 8px rgba(0,0,0,.15);display:flex;align-items:center;justify-content:center}

/* about */
.about-img{left:100px;top:985px;width:420px;height:400px;border-radius:0 30px 0 30px;background:radial-gradient(circle at 45% 55%,#fff3c9 0%,#fbbf5a 35%,#f08a1d 100%)}
.about-p{left:624px;top:1092px;width:490px;font-size:14.5px;line-height:25px;color:var(--text);text-align:justify}
.badge{position:absolute;width:124px;height:124px;border-radius:50%;border:3px solid var(--green);display:flex;align-items:center;justify-content:center}
.badge::before{content:"";position:absolute;inset:7px;border:1px solid var(--green);border-radius:50%}
.badge i{width:52px;height:52px;border-radius:50%;background:var(--green);display:block}

/* products */
.card{position:absolute;width:312px;height:368px;background:var(--white);box-shadow:0 2px 10px rgba(0,0,0,.07);text-align:center}
.card .jar{left:90px;top:35px;width:140px;height:185px}
.card h3{position:absolute;left:0;right:0;top:243px;font-size:16.5px;font-weight:700;letter-spacing:.2px}
.card p{position:absolute;left:0;right:0;top:270px;font-size:15px;font-weight:500}
.card .btn{left:82px;top:306px;width:150px;height:38px;font-size:13px}

/* best sellers */
.seller{position:absolute;top:3379px;height:477px;text-align:center}
.seller h3{margin-top:45px;font-size:18px;font-weight:700;color:#444;white-space:nowrap}
.seller u{display:block;margin-top:10px;font-size:13px;font-weight:700;color:#444}
.seller .jar{left:50%;transform:translateX(-50%);top:130px;width:240px;height:310px}

/* footer */
.footer{position:absolute;left:0;top:4474px;width:1200px;height:397px;background:var(--green);color:var(--white)}
.footer h4{position:absolute;top:80px;font-size:15px;font-weight:700;letter-spacing:.3px}
.footer ul{position:absolute;top:118px;list-style:none;font-size:14px;line-height:33px}
.social{position:absolute;top:292px;width:24px;height:24px;border-radius:50%;background:var(--white)}
.footer-brand{position:absolute;left:100px;top:90px;width:290px;display:flex;flex-direction:column;align-items:center;gap:14px}
.footer-brand .name{font-size:24px;font-weight:500;letter-spacing:3px;white-space:nowrap}
</style>
</head>
<body>

<section class="hero">
  <svg class="hero-clouds" viewBox="0 0 1200 127" preserveAspectRatio="none" aria-hidden="true">
    <path d="M0 40 Q60 0 130 30 Q170 70 240 90 L960 90 Q1040 40 1100 10 Q1160 0 1200 20 L1200 127 L0 127Z" fill="#fff"/>
    <rect x="0" y="107" width="1200" height="20" fill="#f4f6e3"/>
  </svg>
</section>

<nav class="nav">
  <a style="left:128px">HOME</a>
  <a style="left:258px;font-weight:500">SHOP</a>
  <a style="left:380px;font-weight:500">ABOUT US</a>
  <a style="left:811px;font-weight:500">CONTACT US</a>
</nav>
<div class="brand"><i class="dot"></i><span>Marumaru Honey</span></div>
<svg class="abs" style="left:980px;top:60px" width="140" height="26" viewBox="0 0 140 26" aria-label="Search, account and cart">
  <circle cx="11" cy="12" r="7" fill="none" stroke="#222" stroke-width="2"/><line x1="16" y1="17" x2="21" y2="22" stroke="#222" stroke-width="2"/>
  <circle cx="60" cy="8" r="5" fill="none" stroke="#222" stroke-width="2"/><path d="M51 22 Q60 11 69 22Z" fill="none" stroke="#222" stroke-width="2"/>
  <path d="M100 5 L104 5 L108 18 L120 18 L123 9 L106 9" fill="none" stroke="#222" stroke-width="2"/><circle cx="109" cy="22" r="2" fill="#222"/><circle cx="119" cy="22" r="2" fill="#222"/>
  <circle cx="136" cy="4" r="4" fill="var(--green)"/>
</svg>

<div class="abs display" style="left:0;width:1200px;top:268px;text-align:center;font-size:78px;color:var(--green)">SUPER DELICIOUS</div>
<div class="abs display" style="left:0;width:1200px;top:340px;text-align:center;font-size:80px;font-weight:700;letter-spacing:3px">HANDCRAFTED MUNAKA HONEY</div>
<div class="btn btn-green" style="left:523px;top:431px;width:174px;height:45px">Shop Now</div>
<div class="arrow" style="left:56px;top:377px"><svg width="14" height="20"><path d="M10 3 L3 10 L10 17" fill="none" stroke="#333" stroke-width="2"/></svg></div>
<div class="arrow" style="left:1100px;top:377px"><svg width="14" height="20"><path d="M4 3 L11 10 L4 17" fill="none" stroke="#333" stroke-width="2"/></svg></div>
<div class="jar" role="img" aria-label="Honey jar product mockup" style="left:306px;top:563px;width:200px;height:280px"></div>
<div class="jar" role="img" aria-label="Honey jar product mockup" style="left:705px;top:563px;width:200px;height:280px"></div>
<div class="jar" role="img" aria-label="Honey jar product mockup, front" style="left:470px;top:508px;width:260px;height:355px"></div>

<section>
  <div class="abs" style="left:0;top:1410px;width:1200px;height:1312px;background:var(--cream)"></div>
  <svg class="abs" style="left:0;top:1000px" width="1200" height="480" viewBox="0 0 1200 480" preserveAspectRatio="none" aria-hidden="true">
    <path d="M0 460 Q120 380 600 360 Q1000 340 1200 30 L1200 0 L0 0Z" fill="#fff"/>
  </svg>
  <div class="abs about-img" role="img" aria-label="Honey dipper drizzling honey beside a jar on a warm orange glow"></div>
  <div class="jar" role="img" aria-label="Honey jar product mockup" style="left:395px;top:1188px;width:190px;height:245px"></div>
  <h2 class="abs display" style="left:624px;top:1004px;font-size:66px">ABOUT US</h2>
  <p class="abs about-p">Sed ut perspiciatis unde omnis iste natus error sit voluptatem accusantium doloremque laudantium, totam rem aperiam, eaque ipsa quae ab illo inventore veritatis et quasi architecto beatae vitae dicta sunt explicabo. Nemo enim ipsam voluptatem quia voluptas sit aspernatur aut odit aut fugit.</p>
  <div class="badge" role="img" aria-label="No added flavours" style="left:630px;top:1252px"><i></i></div>
  <div class="badge" role="img" aria-label="No added preservatives" style="left:794px;top:1252px"><i></i></div>
  <div class="badge" role="img" aria-label="Quality and healthy" style="left:957px;top:1252px"><i></i></div>
</section>

<section>
  <h2 class="abs display" style="left:0;width:1200px;top:1632px;text-align:center;font-size:72px">SHOP NOW OUR PRODUCTS</h2>
  <div class="card" style="left:96px;top:1739px"><div class="jar" role="img" aria-label="Cashew carob jar"></div><h3>CASHEW CAROB</h3><p>$10.99 USD</p><div class="btn btn-green">Shop Now</div></div>
  <div class="card" style="left:435px;top:1739px"><div class="jar" role="img" aria-label="Carob hazelnut jar"></div><h3>CAROB HAZELNUT</h3><p>$30.99 USD</p><div class="btn btn-green">Shop Now</div></div>
  <div class="card" style="left:777px;top:1739px"><div class="jar" role="img" aria-label="Honey glazed roasted jar"></div><h3>HONEY GLAZED ROASTED</h3><p>$20.99 USD</p><div class="btn btn-green">Shop Now</div></div>
  <div class="card" style="left:100px;top:2143px"><div class="jar" role="img" aria-label="Cashew carob jar"></div><h3>CASHEW CAROB</h3><p>$10.99 USD</p><div class="btn btn-green">Shop Now</div></div>
  <div class="card" style="left:439px;top:2143px"><div class="jar" role="img" aria-label="Carob hazelnut jar"></div><h3>CAROB HAZELNUT</h3><p>$30.99 USD</p><div class="btn btn-green">Shop Now</div></div>
  <div class="card" style="left:781px;top:2143px"><div class="jar" role="img" aria-label="Honey glazed roasted jar"></div><h3>HONEY GLAZED ROASTED</h3><p>$20.99 USD</p><div class="btn btn-green">Shop Now</div></div>
  <div class="btn btn-outline" style="left:478px;top:2578px;width:246px;height:50px">View All Products</div>
</section>

<section class="abs" style="left:0;top:2722px;width:1200px;height:482px;background:var(--video-bg)">
  <h2 class="abs display" style="left:127px;top:112px;font-size:66px">OUR VIDEO</h2>
  <p class="abs" style="left:127px;top:180px;width:448px;font-size:14.5px;line-height:25px;color:var(--text);text-align:justify">Sed ut perspiciatis unde omnis iste natus error sit voluptatem accusantium doloremque laudantium, totam rem aperiam, eaque ipsa quae ab illo inventore veritatis et quasi architecto beatae vitae dicta sunt explicabo. Nemo enim ipsam voluptatem quia voluptas sit aspernatur aut odit aut fugit.</p>
  <div class="btn btn-outline" style="left:124px;top:336px;width:186px;height:44px;font-size:13px">Learn More</div>
  <div class="abs" role="img" aria-label="Beekeeper lifting a honeycomb frame from a hive" style="left:612px;top:88px;width:482px;height:303px;background:linear-gradient(135deg,#4a3b26,#c8902f 45%,#e9b94a 60%,#5a4a30)"></div>
  <svg class="abs" style="left:812px;top:198px" width="82" height="82" viewBox="0 0 82 82" aria-label="Play video">
    <circle cx="41" cy="41" r="37" fill="none" stroke="#fff" stroke-width="5"/><path d="M32 24 L60 41 L32 58Z" fill="#fff"/>
  </svg>
</section>

<h2 class="abs display" style="left:0;width:1200px;top:3280px;text-align:center;font-size:72px">BEST SELLERS</h2>
<div class="seller" style="left:0;width:395px;background:var(--purple)"><h3>HONEY GLAZED MANUKA</h3><u>SHOP NOW</u><div class="jar" role="img" aria-label="Honey glazed manuka jar"></div></div>
<div class="seller" style="left:399px;width:400px;background:var(--lime)"><h3>MAPLE MARUMARU MANUKA</h3><u>SHOP NOW</u><div class="jar" role="img" aria-label="Maple manuka jar"></div></div>
<div class="seller" style="left:803px;width:397px;background:var(--blue)"><h3>MARUMARU MANUKA</h3><u>SHOP NOW</u><div class="jar" role="img" aria-label="Manuka honey jar"></div></div>

<section class="abs" style="left:0;top:3856px;width:1200px;height:618px;background:#fbfaf8">
  <div class="abs" role="img" aria-label="Smiling woman in a kitchen spooning honey from a jar" style="left:560px;top:0;width:640px;height:618px;background:linear-gradient(120deg,#fbfaf8 0%,#f3e4d6 25%,#e9b99a 55%,#d95a3e 80%,#c8443a 100%)"></div>
  <h2 class="abs display" style="left:97px;top:148px;font-size:64px;line-height:58px">BEST PRODUCT<br>FOR YOUR FAMILY</h2>
  <p class="abs" style="left:100px;top:286px;width:380px;font-size:14px;line-height:25px;color:var(--text);text-align:justify">At vero eos et accusamus et iusto odio dignissimos ducimus qui blanditiis praesentium voluptatum deleniti atque corrupti .</p>
  <div class="btn btn-outline" style="left:97px;top:384px;width:166px;height:44px;font-size:12px">Shop Now</div>
  <div class="jar" role="img" aria-label="Honey jar product mockup" style="left:430px;top:400px;width:135px;height:175px"></div>
</section>

<footer class="footer">
  <div class="footer-brand">
    <i style="width:40px;height:40px;border-radius:50%;background:var(--white);display:block"></i>
    <span class="name">MARUMARU HONEY</span>
    <span style="font-size:12px;letter-spacing:2px;margin-top:-12px">CO.</span>
  </div>
  <p class="abs" style="left:107px;top:233px;font-size:14px">Copyright © 2020 Marumaru Honey</p>
  <p class="abs" style="left:110px;top:262px;font-size:12.5px">Privacy &nbsp;|&nbsp; Terms of Use</p>
  <i class="social" style="left:110px"></i><i class="social" style="left:149px"></i><i class="social" style="left:188px"></i><i class="social" style="left:227px"></i>
  <h4 style="left:438px">NAVIGATE</h4>
  <ul style="left:440px"><li>Home</li><li>About Us</li><li>Products</li><li>Shop Now</li><li>Cotnact Us</li></ul>
  <h4 style="left:632px">RESOURCES</h4>
  <ul style="left:634px"><li>Privacy Policy</li><li>Terms</li><li>My Account</li><li>Shipping &amp; Return</li><li>Cart</li></ul>
  <h4 style="left:853px">CONNECT WITH US</h4>
  <p class="abs" style="left:856px;top:124px;font-size:14px">Sign up here to stay up to date</p>
  <div class="abs" style="left:855px;top:160px;width:258px;height:40px;background:var(--white);color:#999;font-size:11px;display:flex;align-items:center;padding-left:20px;letter-spacing:.5px">EMAIL ADDRESS</div>
  <div class="btn" style="left:857px;top:212px;width:258px;height:42px;background:#111;color:var(--white);font-size:14px;font-weight:600">Subscribe</div>
</footer>

</body>
</html>
```